Halvard Quarry Company needs a company newsletter template

We need a 2-page editable newsletter template, that we can update monthly with various information and pictures. We would like an area to include our values: Be Safe, Be Honest, Be Responsible, Be Respectful, Be Great. Ideally we would have 2-3 bulk text areas to highlight different things each month, with area we an update a picture from time to time and maybe some text areas where we can add a fun fact type thing. Some of the areas we will include are production milestones (if any), monthly tenure, monthly new hires, highlighting an employee that demonstrates our value, community engagement, upcoming holidays/events, press releases. The exact content will likely change month to month but these will be some of the frequent topics. We are a copper Mine in northern Yukon. I've attached our Brand Guidelines and logo files. Our website is brelcoreworks.com if you want to see the style and type of photos from our site

```html
<!DOCTYPE html>
<html lang="en">
<head>
<meta charset="utf-8">
<title>Halvard Quarry Company Newsletter Template</title>
<link href="https://fonts.googleapis.com/css2?family=Montserrat:wght@300;400;600;700;800;900&family=Rubik:wght@800&family=Tinos:ital@1&display=swap" rel="stylesheet">
<style>
  :root{
    --rust:#8a3a2c;
    --navy:#243246;
    --gold:#f0c12c;
    --gold-text:#ecc229;
    --ink:#3b3431;
    --paper:#ffffff;
    --backdrop:#efeeeb;
  }
  *{box-sizing:border-box;margin:0;padding:0}
  html,body{width:1200px;height:961px;overflow:hidden;background:var(--backdrop)}
  body{position:relative;font-family:'Montserrat',sans-serif;color:var(--ink)}

  .page{position:absolute;width:448px;height:580px;background:var(--paper);overflow:hidden}
  .page--front{left:117px;top:61px}
  .page--back{left:634px;top:319px}

  /* masthead */
  .masthead{position:absolute;left:0;top:0;width:448px;height:75px}
  .masthead__brand{position:absolute;left:0;top:0;width:83px;height:75px;background:var(--rust);
    display:flex;flex-direction:column;align-items:center;justify-content:center;gap:5px;padding:0 6px}
  .masthead__mark{width:9px;height:9px;background:var(--gold)}
  .masthead__name{font-weight:700;font-size:7.2px;line-height:1.15;color:#fff;text-align:center;letter-spacing:.2px;text-transform:uppercase}
  .masthead__title{position:absolute;left:83px;top:0;width:365px;height:58px;background:var(--navy);
    color:var(--gold-text);font-weight:300;font-size:47px;line-height:58px;padding-left:19px;letter-spacing:.6px}
  .masthead__values{position:absolute;left:83px;top:58px;width:365px;height:17px;background:var(--gold);
    color:var(--navy);font-size:8.6px;line-height:17px;text-align:center;letter-spacing:-.05px}

  /* front page */
  .hero{position:absolute;left:0;top:75px;width:448px;height:210px;
    background:linear-gradient(180deg,#5c93cf 0%,#a9c8e6 45%,#c7c1ad 62%,#6f5c4a 84%,#4a3c31 100%)}
  .hero__headline{position:absolute;left:21px;top:26px;font-size:21.5px;line-height:21px;color:var(--navy);font-weight:400}
  .hero__headline strong{color:var(--rust);font-weight:900}

  .lead{position:absolute;left:21px;top:305px;width:262px;font-size:7.3px;line-height:10.1px}
  .lead p+p{margin-top:10.1px}
  .dropcap{float:left;font-size:37px;line-height:30px;font-weight:300;color:var(--rust);margin:1px 4px 0 0}

  .sidebar{position:absolute;left:293px;top:258px;width:155px;height:322px;background:var(--rust)}
  .section-head{display:flex;gap:5px;font-family:'Rubik',sans-serif;font-weight:800;font-size:13.2px;line-height:15px}
  .section-head__tag{flex:none;width:10px;height:10px;margin-top:2px}
  .section-head__top{color:#fff}
  .section-head__bottom{display:block;color:var(--gold)}
  .sidebar .section-head{position:absolute;left:4px;top:2px}
  .sidebar__photo{position:absolute;left:14px;top:42px;width:120px;height:94px;
    background:linear-gradient(180deg,#c99a6b 0%,#6d5346 50%,#3b332f 100%)}
  .sidebar__text{position:absolute;left:14px;top:148px;width:124px;height:170px;overflow:hidden;
    font-family:'Tinos',serif;font-style:italic;font-size:6.7px;line-height:8.1px;color:#fff}
  .sidebar__text p+p{margin-top:8px}

  /* back page */
  .feature{position:absolute;left:0;top:75px;width:448px;height:246px;background:var(--rust);color:#fff}
  .feature__col{position:absolute;top:14px;width:194px;height:228px;overflow:hidden;font-size:7.3px;line-height:10.1px}
  .feature__col--left{left:20px}
  .feature__col--right{left:234px}
  .feature__col p+p{margin-top:10.1px}
  .feature .dropcap{color:#fff}

  .briefs{position:absolute;left:0;top:321px;width:448px;height:259px}
  .brief{position:absolute;top:8px;width:130px}
  .brief:nth-child(1){left:6px}
  .brief:nth-child(2){left:149px}
  .brief:nth-child(3){left:293px}
  .brief .section-head__top{color:var(--rust)}
  .brief__text{margin:10px 0 0 15px;width:122px;height:200px;overflow:hidden;
    font-family:'Tinos',serif;font-style:italic;font-size:6.7px;line-height:8.1px;color:var(--ink)}
  .brief__text p+p{margin-top:8px}
</style>
</head>
<body>

<section class="page page--front">
  <header class="masthead">
    <div class="masthead__brand"><span class="masthead__mark"></span><span class="masthead__name">Halvard Quarry Company</span></div>
    <h1 class="masthead__title">NEWSLETTER</h1>
    <p class="masthead__values">BE SAFE, BE HONEST, BE RESPONSIBLE, BE RESPECTFUL, BE GREAT.</p>
  </header>

  <div class="hero" role="img" aria-label="Photo of a yellow haul truck and a dragline crane at an open-pit mine under a blue sky">
    <h2 class="hero__headline"><strong>TITTLE HERE</strong> AMET<br>LOREMIPSUM<br><strong>DOLORSIT</strong></h2>
  </div>

  <article class="lead">
    <p><span class="dropcap">L</span>orem ipsum dolor sit amet, consectetur adipiscing elit. Duis risus libero, condimentum in molestie quis, gravida non justo. Integer aliquam tellus id nisl fringilla sollicitudin. Curabitur non condimentum diam. Morbi suscipit, risus non maximus semper, elit nisl placerat augue, id pharetra nulla neque ac diam. Curabitur eu malesuada nunc. Phasellus in aliquam lectus, et blandit enim. Mauris dignissim varius tortor, et tincidunt augue euismod sit amet. In hac habitasse platea dictumst. Praesent enim est, rutrum et velit quis, lobortis cursus dui. Praesent ultrices, mi in molestie efficitur, est urna scelerisque nunc, quis vestibulum eros risus vitae lectus.</p>
    <p>Nulla id vehicula tellus. Duis vitae consequat dolor. Fusce ultricies tortor ipsum, ac tempus mi iaculis et. Fusce quis fermentum enim. Curabitur tempus suscipit faucibus. Sed eu cursus orci, tincidunt tincidunt turpis. Vestibulum ante ipsum primis in faucibus orci luctus et ultrices posuere cubilia curae; Donec turpis turpis, pretium non elit quis, fermentum dignissim massa. Nam vitae odio non augue mattis malesuada. Etiam est diam, ullamcorper lacinia rhoncus quis, gravida venenatis magna.</p>
    <p>Nunc pretium libero hendrerit justo consectetur ornare. Etiam dictum metus id turpis volutpat, nec interdum ipsum pharetra. Sed et vestibulum dolor. Nam sapien nibh, dictum nec lacinia non, laoreet in nulla. Vestibulum molestie dignissim tristique. Nulla pellentesque urna leo, nec malesuada diam elementum elementum. Proin eget ipsum.</p>
  </article>

  <aside class="sidebar">
    <h3 class="section-head">
      <svg class="section-head__tag" viewBox="0 0 10 10"><rect width="10" height="10" fill="#243246"/><path d="M0 10 L10 0 L10 10 Z" fill="#f0c12c"/></svg>
      <span><span class="section-head__top">Monthly</span><span class="section-head__bottom">New Hires</span></span>
    </h3>
    <div class="sidebar__photo" role="img" aria-label="Photo of a new hire in a hard hat and safety vest holding a clipboard at the mine site"></div>
    <div class="sidebar__text">
      <p>Lorem ipsum dolor sit amet, consectetur adipiscing elit. Duis risus libero, condim enin. Curabitur non condimentum diam. Morbi suscipit, risus non maximus semper, elit nisl placerat augue.</p>
      <p>Nulla id vehicula tellus. Duis vitae cons equat dolor. Fusce ultricies tortor ipsum, aam est diam, ullamcorper lacinia rhon cus quis, gravida venenatis magna.</p>
      <p>Nunc pretium libero hendrerit justo cons ectetur ornare. Etiam dictum metus id turpis volutpat, nec interdum ipsum phaas retra. tibulum molestie dignissim tristas ique. Nulla pellentesque urna leo, nema l esuada diam elementum elementum. Proin eget ipsum</p>
    </div>
  </aside>
</section>

<section class="page page--back">
  <header class="masthead">
    <div class="masthead__brand"><span class="masthead__mark"></span><span class="masthead__name">Halvard Quarry Company</span></div>
    <h1 class="masthead__title">NEWSLETTER</h1>
    <p class="masthead__values">BE SAFE, BE HONEST, BE RESPONSIBLE, BE RESPECTFUL, BE GREAT.</p>
  </header>

  <article class="feature">
    <div class="feature__col feature__col--left">
      <p><span class="dropcap">L</span>orem ipsum dolor sit amet, consectetur adipiscing elit. Duis risus libero, condi ment um in molestie quis, gravida non justo. Integ er aliquam tellus id nisl fringilla sollicitudin. Curabitur non condimentum diam. Morbi suscipit, risus non maximus semper, elit nisl placerat augue, id pharetra nulla neque ac diam. Curabitur eu malesuada nunc. Phasellus in aliquam lectus, et blandit enim. Mauris dignissim varius tortor, et tincidunt augue euismod sit amet. In hac habitasse platea dictumst. Praesent enim est, rutrum et velit quis, lobortis cursus dui.</p>
      <p>Nulla id vehicula tellus. Duis vitae consequat dolor. Fusce ultricies tortor ipsum, ac tempus mi iaculis et. Fusce quis fermentum enim. Curabitur tempus suscipit faucibus. Sed eu cursus orci, tincidunt tincidunt turpis. Vest fermentum enim. Curabitur tempus suscipit faucibus. Sed eu cursus orci, tincidunt tincidunt turpis. Vestibuluibulum ante ipsum primis in faucibus orci luctus et ultrices posuere cubilia curae; Donec turpis turpis, pretium</p>
    </div>
    <div class="feature__col feature__col--right">
      <p>non elit quis, fermentum dignissim massa. Nam vitae odio non augue mattis malesuada. Etiam est diam, ullamc orper lacinia rhoncus quis, gravida venenatis magna. Nunc pretium libero hendrerit justo consectetur ornare. Etiam dictum metus id turpis volutpat, nec interdum ipsum pharetra. Sed et vestibulum dolor. Nam sapien nibh, dictum nec lacinia non, laoreet in nulla. Vestibulum molestie dignissim tristique. Nulla pellentesque urna leo, nec malesuada diam elementum elementum. Proin eget ipsum ligula.</p>
      <p>Donec fringilla, turpis sed convallis vestibulum, nunc augue hendrerit enim, ac fermentum arcu lorem at lectus. Sed ultricies lobortis neque, a porta est pre ium id. Sed magna s massa. Sed in mauris ac ante cursus pul vinar. Aenean molestie congueem, laoreet vitae viverra ut, lacinia in massa. Sed in mauris ac ante cursus pul vinar. Aenean molestie congue erat, nec porttitor urna vel ue et. Nam auctor purus lorem, vitae pharetra mi dapibus non. Ut mollis neque vita.</p>
    </div>
  </article>

  <div class="briefs">
    <section class="brief">
      <h3 class="section-head">
        <svg class="section-head__tag" viewBox="0 0 10 10"><rect width="10" height="10" fill="#8a3a2c"/><path d="M0 10 L10 0 L10 10 Z" fill="#f0c12c"/></svg>
        <span><span class="section-head__top">Production</span><span class="section-head__bottom">Milestones</span></span>
      </h3>
      <div class="brief__text">
        <p>Lorem ipsum dolor sit amet, consectetur adipiscing elit. Duis risus libero, condim enin. Curabitur non condimentum diam. Morbi suscipit, risus non maximus semper, elit nisl placerat augue.</p>
        <p>Nulla id vehicula tellus. Duis vitae cons equequat dolor. Fusce ultricies tortor ipsu m, aam est diat dolor. Fusce ul tri cies tortor ipsu m, aam est diam, ul lam corper lacinia rhon cus quis, gravida venenatis</p>
        <p>Nunc pretium libero hendrerit justo cons ectetur dignissim tristas ique. Nulla pellentesque urna leo, nema l esuada diam elementum elementum. Proin eget ipsum nec interdum ipsum phaas retra. tibulum molestie dignissim tristas ique. Nulla pellentesque urna leo, nema l esuada diam elementum elemen tum. Proin eget ipsum nec interdum ipsu m phaas retra. tibulum molestie dign iss im tristas ique. Nulla pellentesque urna</p>
      </div>
    </section>
    <section class="brief">
      <h3 class="section-head">
        <svg class="section-head__tag" viewBox="0 0 10 10"><rect width="10" height="10" fill="#8a3a2c"/><path d="M0 10 L10 0 L10 10 Z" fill="#f0c12c"/></svg>
        <span><span class="section-head__top">Press</span><span class="section-head__bottom">Releases</span></span>
      </h3>
      <div class="brief__text">
        <p>Lorem ipsum dolor sit amet, consectetur adipiscing elit. Duis risus libero, condim enin. Curabitur non condimentum diam. Morbi suscipit, risus non maximus semper, elit nisl placerat augue.</p>
        <p>Nulla id vehicula tellus. Duis vitae cons equequat dolor. Fusce ultricies tortor ipsu m, aam est diat dolor. Fusce ul tri cies tortor ipsu m, aam est diam, ul lam corper lacinia rhon cus quis, gravida venenatis</p>
        <p>Nunc pretium libero hendrerit justo cons ectetur dignissim tristas ique. Nulla pellentesque urna leo, nema l esuada diam elementum elementum. Proin eget ipsum nec interdum ipsum phaas retra. tibulum molestie dignissim tristas ique. Nulla pellentesque urna leo, nema l esuada diam elementum elemen tum. Proin eget ipsum nec interdum ipsu m phaas retra. tibulum molestie dign iss im tristas ique. Nulla pellentesque urna</p>
      </div>
    </section>
    <section class="brief">
      <h3 class="section-head">
        <svg class="section-head__tag" viewBox="0 0 10 10"><rect width="10" height="10" fill="#8a3a2c"/><path d="M0 10 L10 0 L10 10 Z" fill="#f0c12c"/></svg>
        <span><span class="section-head__top">Upcoming</span><span class="section-head__bottom">Holidays/events</span></span>
      </h3>
      <div class="brief__text">
        <p>Lorem ipsum dolor sit amet, consectetur adipiscing elit. Duis risus libero, condim enin. Curabitur non condimentum diam. Morbi suscipit, risus non maximus semper, elit nisl placerat augue.</p>
        <p>Nulla id vehicula tellus. Duis vitae cons equequat dolor. Fusce ultricies tortor ipsu m, aam est diat dolor. Fusce ul tri cies tortor ipsu m, aam est diam, ul lam corper lacinia rhon cus quis, gravida venenatis</p>
        <p>Nunc pretium libero hendrerit justo cons ectetur dignissim tristas ique. Nulla pellentesque urna leo, nema l esuada diam elementum elementum. Proin eget ipsum nec interdum ipsum phaas retra. tibulum molestie dignissim tristas ique. Nulla pellentesque urna leo, nema l esuada diam elementum elemen tum. Proin eget ipsum nec interdum ipsu m phaas retra. tibulum molestie dign iss im tristas ique. Nulla pellentesque urna</p>
      </div>
    </section>
  </div>
</section>

</body>
</html>
```